Flyer für Alltagsbegleitung
Zielgruppe
Firma: Tageshilfe Sonnenweg
Meine Zielgruppe sind alle Menschen, die im Alltag, Hilfe benötigen.
Aufgabenstellung
Der Flyer soll modern und und ansprechend aussehen. Es soll vermerkt sein, das ich als annerkannte Kraft, Entlastungsleistung nach

```html
<!DOCTYPE html>
<html lang="de">
<head>
<meta charset="utf-8">
<title>Flyer – Tageshilfe Sonnenweg</title>
<link href="https://fonts.googleapis.com/css2?family=Montserrat:wght@400;500;600;700;800&display=swap" rel="stylesheet">
<style>
  :root {
    --page: #eeebe5;
    --paper: #ffffff;
    --navy: #2d3f5e;
    --blue: #4d6d97;
    --blue-soft: #dde6f0;
    --blue-mid: #b8c9de;
    --peach: #f1b07a;
    --text: #34435d;
    --muted: #5f6e85;
  }
  * { box-sizing: border-box; margin: 0; padding: 0; }
  html, body { width: 1200px; height: 791px; overflow: hidden; }
  body {
    background: var(--page);
    font-family: "Montserrat", sans-serif;
    color: var(--text);
  }
  .flyer {
    position: absolute; left: 75px; top: 60px;
    width: 1050px; height: 670px;
    display: flex;
    box-shadow: 0 8px 30px rgba(40,50,70,.15);
  }
  .panel { width: 350px; height: 100%; position: relative; overflow: hidden; }

  /* cover */
  .cover { background: var(--paper); }
  .brand { position: absolute; left: 26px; top: 24px; display: flex; align-items: center; gap: 8px;
    font-size: 13px; font-weight: 600; color: var(--navy); }
  .brand-dot { width: 12px; height: 12px; border-radius: 50%; background: var(--blue); }
  .cover-photo { position: absolute; left: 26px; top: 60px; width: 324px; height: 220px;
    border-radius: 22px 0 0 0; background: linear-gradient(135deg, #8d9aab, #c9c3ba 55%, #4f6f98); }
  .cover-band { position: absolute; left: 26px; top: 280px; width: 324px; height: 362px;
    background: var(--blue); border-radius: 0 0 0 22px; padding: 70px 28px 0; color: #fff; }
  .cover-title { font-size: 21px; font-weight: 800; letter-spacing: .04em; text-transform: uppercase; }
  .cover-sub { margin-top: 8px; font-size: 19px; font-weight: 500; line-height: 1.35; }
  .cover-web { position: absolute; left: 28px; bottom: 40px; font-size: 10px; font-weight: 600; letter-spacing: .05em; }
  .cover-icon { position: absolute; right: 28px; bottom: 28px; }

  /* about */
  .about { background: var(--blue-soft); padding: 44px 34px 0; }
  .quote { font-size: 15px; font-weight: 700; line-height: 1.4; text-transform: uppercase; color: var(--navy); }
  .quote-author { margin-top: 6px; font-size: 10px; color: var(--muted); }
  .about-heading { margin-top: 34px; font-size: 13px; font-weight: 800; letter-spacing: .05em; color: var(--navy); }
  .about-text { margin-top: 14px; font-size: 11.5px; line-height: 1.65; color: var(--text); }
  .portrait { position: absolute; left: 130px; top: 470px; width: 90px; height: 100px;
    border-radius: 10px; background: linear-gradient(160deg, #e9dccd, #c9a983); }
  .web-button { position: absolute; left: 34px; right: 34px; top: 592px; height: 32px; border-radius: 16px;
    background: #fff; display: flex; align-items: center; justify-content: center;
    font-size: 9.5px; font-weight: 700; letter-spacing: .06em; color: var(--navy); }

  /* contact */
  .contact { background: var(--paper); padding: 30px 24px; }
  .contact-photo { height: 250px; border-radius: 16px; background: linear-gradient(150deg, #7e9a6e, #d8d4cf 55%, #9fa9c4); }
  .contact-tag { display: inline-block; margin-top: 64px; margin-left: 18px; background: var(--navy); color: #fff;
    font-size: 11px; font-weight: 700; letter-spacing: .08em; padding: 7px 18px; border-radius: 10px 10px 0 0; }
  .contact-box { background: var(--peach); padding: 20px 22px 22px; border-radius: 4px; position: relative; color: var(--navy); }
  .contact-name { font-size: 14px; font-weight: 700; }
  .contact-line { font-size: 11px; margin-top: 6px; }
  .contact-line.small { font-size: 9.5px; font-weight: 600; letter-spacing: .04em; }
  .contact-company { margin-top: 26px; font-size: 14px; font-weight: 700; }
  .contact-web { margin-top: 14px; font-size: 9.5px; font-weight: 700; letter-spacing: .05em; }
  .contact-icon { position: absolute; right: 20px; bottom: 46px; width: 34px; height: 34px; border-radius: 50%;
    border: 2px solid var(--navy); }
</style>
</head>
<body>
  <main class="flyer">
    <section class="panel cover">
      <div class="brand"><span class="brand-dot"></span>Lena Brandt</div>
      <div class="cover-photo" role="img" aria-label="Foto: Betreuerin im Gespräch mit einem älteren Herrn"></div>
      <div class="cover-band">
        <h1 class="cover-title">Alltagsbegleitung</h1>
        <p class="cover-sub">Mit Herz, Verlässlichkeit<br>&amp; Erfahrung</p>
        <p class="cover-web">WWW.TAGESHILFE-SONNENWEG.DE</p>
        <svg class="cover-icon" width="44" height="40" viewBox="0 0 44 40" fill="none" stroke="#fff" stroke-width="1.8">
          <path d="M22 36 C6 25 3 17 3 11 C3 5 8 2 13 2 C17 2 20 4 22 8 C24 4 27 2 31 2 C36 2 41 5 41 11 C41 17 38 25 22 36 Z"/>
        </svg>
      </div>
    </section>

    <section class="panel about">
      <p class="quote">„Sich um diejenigen zu kümmern, die sich einst um uns gekümmert haben, ist eine der grössten Ehren.“</p>
      <p class="quote-author">– Mara Sommer</p>
      <h2 class="about-heading">WER BIN ICH?</h2>
      <p class="about-text">Mein Name ist Lena Brandt. Als anerkannte Betreuungskraft nach § 45a SGB XI unterstütze ich Menschen mit Pflegegrad im Alltag – flexibel, menschlich und individuell. Ich biete Hilfe im Haushalt, Begleitung zu Terminen oder einfach nur ein offenes Ohr – ganz nach Ihren Bedürfnissen.</p>
      <div class="portrait" role="img" aria-label="Porträtfoto der Betreuerin"></div>
      <div class="web-button">ERFAHRE MEHR AUF UNSERER WEBSITE</div>
    </section>

    <section class="panel contact">
      <div class="contact-photo" role="img" aria-label="Foto: Betreuerin begleitet eine ältere Dame mit Rollator im Garten"></div>
      <span class="contact-tag">KONTAKT</span>
      <div class="contact-box">
        <p class="contact-name">Lena Brandt</p>
        <p class="contact-line">Phone: 0151 2468 1357</p>
        <p class="contact-line small">E-MAIL: KONTAKT@TAGESHILFE-SONNENWEG.DE</p>
        <p class="contact-company">Tageshilfe Sonnenweg</p>
        <p class="contact-line">Lindenweg 12, 12345 Musterstadt</p>
        <p class="contact-web">WWW.TAGESHILFE-SONNENWEG.DE</p>
        <div class="contact-icon" role="img" aria-label="Symbol: helfende Person"></div>
      </div>
    </section>
  </main>
</body>
</html>
```